Fundrally Slides

I need a graphic designer go through the attached power point presentation (4 slides) and make it look clean, modern, and branded.

The four slides are currently displayed as jpegs on the Fundrally viewing page below -
Here is the Fundrally preview link:: https://www.fundrally.example/projects/4826153907/5390284716?token=3c7a91f2
Updates

Project Deadline Extended

Industry/Entity Type

Graphic Designer

Requirements
Must have
• Simple, clean same color scheme as logo

```html
<!DOCTYPE html>
<html lang="en">
<head>
<meta charset="utf-8">
<title>Fundrally Slides</title>
<link href="https://fonts.googleapis.com/css2?family=Lato:wght@300;400;700;900&display=swap" rel="stylesheet">
<style>
  :root{
    --stage:#2b2b2b;
    --brand:#0033a0;
    --ink:#222;
    --paper:#fff;
    --bar:#000;
    --pie-blue:#4f81bd;
    --pie-red:#c0504d;
    --pie-green:#9bbb59;
    --pie-purple:#8064a2;
    --pie-teal:#4bacc6;
  }
  *{box-sizing:border-box;margin:0;padding:0}
  html,body{width:800px;height:1200px;overflow:hidden;background:var(--stage)}
  body{position:relative;font-family:'Lato',sans-serif;color:var(--ink)}
  .slide{position:absolute;left:80px;width:640px;height:480px;background:var(--paper);box-shadow:0 2px 8px rgba(0,0,0,.4);overflow:hidden}
  .slide--facts{top:67px}
  .slide--business{top:654px}
  .header{position:absolute;left:0;top:0;width:250px;height:48px}
  .header-title{position:absolute;left:62px;top:20px;font-size:16.5px;font-weight:400;color:#fff;line-height:20px}
  .footer{position:absolute;left:0;bottom:0;width:640px;height:24px;background:var(--bar)}
  .footer-company{position:absolute;left:31px;top:5px;color:#fff;font-weight:700;font-size:11px}
  .footer-product{position:absolute;right:0;top:0;width:160px;height:24px;background:var(--brand);color:#fff;font-weight:900;font-size:8.5px;letter-spacing:.5px;text-align:center;line-height:24px}
  .section-label{position:absolute;left:32px;top:64px;font-size:10.5px;font-weight:700;line-height:14px}
  .icon{position:absolute;left:32px}
  .facts-list{position:absolute;left:64px;top:97px;width:256px;list-style:none;font-size:9.8px;font-weight:300;line-height:13.6px;color:var(--ink)}
  .facts-list li{margin-bottom:13px}
  .accent{color:var(--brand);font-weight:400}
  .chart-card{position:absolute;left:325px;top:96px;width:297px;height:272px;border:1px solid #ccc;border-radius:3px;box-shadow:0 0 3px rgba(0,0,0,.15);padding:5px 4px;font-family:'Lato',sans-serif}
  .chart-title{font-size:7.5px;font-weight:700;color:#333;margin-bottom:6px}
  .chart-intro{font-size:5.3px;line-height:7px;color:#333}
  .chart-intro ul{margin-left:14px;margin-top:2px}
  .chart-intro li{margin-bottom:3px}
  .chart-svg{position:absolute;left:0;top:90px}
  .chart-label{font-family:Georgia,serif;font-size:4.6px;font-weight:700;fill:#333}
  .agency-mark{position:absolute;left:6px;top:195px;width:70px;height:40px;background:var(--brand);color:#fff;font-family:'Lato',sans-serif;font-weight:700;font-size:13px;display:flex;align-items:center;justify-content:center}
  .chart-caption{position:absolute;left:3px;right:3px;bottom:6px;font-size:5.3px;line-height:7px;color:#333}
  .chart-caption a{color:var(--brand)}
  .business-copy{position:absolute;left:64px;top:66px;width:376px;font-size:8.6px;line-height:11.6px;font-weight:400}
  .business-copy p{margin-bottom:11px}
  .business-copy .indent{margin-left:16px}
  .callout{width:303px;height:23px;margin:2px 0 13px 43px;background:var(--brand);color:#fff;font-size:10.5px;text-align:center;line-height:23px}
  .cost-list{list-style:none}
  .seal{position:absolute;left:454px;top:67px;width:164px;height:164px;border-radius:50%;background:#1f2a5a;border:3px solid #e0862a}
  .agency-badge{position:absolute;left:448px;top:275px;width:180px;height:108px;border-radius:50%;background:#eef0f3;border:5px solid #9aa2ad;display:flex;align-items:center;justify-content:center;font-weight:700;font-size:15px;color:#111;text-align:center;line-height:17px}
</style>
</head>
<body>

<section class="slide slide--facts">
  <svg class="header" viewBox="0 0 250 48" aria-hidden="true">
    <path d="M0 48 L0 34 Q22 28 30 0 L244 0 Q230 44 190 46 L0 48 Z" fill="var(--brand)"/>
    <path d="M0 34 Q22 28 30 0 L40 0 Q28 36 0 44 Z" fill="#fff" opacity=".25"/>
  </svg>
  <h1 class="header-title">The Facts</h1>

  <h2 class="section-label">National Health Safety Bureau Statistics</h2>
  <svg class="icon" style="top:88px" width="26" height="26" viewBox="0 0 26 26" aria-hidden="true">
    <circle cx="13" cy="13" r="11.5" fill="none" stroke="var(--brand)" stroke-width="1.6"/>
    <text x="13" y="17" text-anchor="middle" font-family="Lato,sans-serif" font-size="12" font-weight="700" fill="var(--brand)">?</text>
  </svg>

  <ul class="facts-list">
    <li><span class="accent">-&gt;</span> 385,000 percutaneous injuries occur in US hospitals annually.</li>
    <li><span class="accent">-&gt;</span> It's documented that half or more injuries go unreported.</li>
    <li><span class="accent">-&gt; Those injured include:</span> nursing staff, laboratory staff, physicians, housekeepers, and other health care workers.</li>
    <li><span class="accent">-&gt;</span> National Health Safety Bureau defines a “Sharps Injury” as a penetrating stab wound from a needle, scalpel, or other sharp object that may result in exposure to blood or other body fluids.</li>
    <li><span class="accent">-&gt;</span> A report from the Sharps Exposure Reporting Network (SERNet) found that nearly half of all sharps injuries occurred during use of the sharp, and of the nearly 40% of needle injuries which involved a safety designed needle, the majority occurred before activating the safety device.</li>
    <li><span class="accent">-&gt;</span> 24% of injuries caused by a suture needle.</li>
    <li><span class="accent">-&gt;</span> 22% of Sharps Injuries are caused by surgical staples or like sharps.</li>
  </ul>

  <figure class="chart-card">
    <div class="chart-title">How do sharps injuries occur?</div>
    <div class="chart-intro">
      In addition to the use of sharps devices, injuries are also closely associated with certain work practices that can pose an increased risk of bloodborne pathogen exposure. These work practices include:
      <ul>
        <li>Disposal-related activities (11%)</li>
        <li>Activities after use and prior to disposal, such as item disassembly (30%)</li>
        <li>Recapping a used needle (3%)</li>
      </ul>
    </div>
    <svg class="chart-svg" width="297" height="150" viewBox="0 0 297 150" role="img" aria-label="Pie chart of activities associated with percutaneous injuries">
      <g transform="translate(145,78)" stroke="#333" stroke-width=".4">
        <path d="M0 0 L-9.2 -65.4 A66 66 0 0 1 65 11.5 Z" fill="var(--pie-red)"/>
        <path d="M0 0 L65 11.5 A66 66 0 0 1 42.8 50.3 Z" fill="var(--pie-green)"/>
        <path d="M0 0 L42.8 50.3 A66 66 0 0 1 32.6 57.4 Z" fill="var(--pie-purple)"/>
        <path d="M0 0 L32.6 57.4 A66 66 0 0 1 0.9 66 Z" fill="var(--pie-teal)"/>
        <path d="M0 0 L0.9 66 A66 66 0 0 1 -9.2 -65.4 Z" fill="var(--pie-blue)"/>
      </g>
      <g stroke="#333" stroke-width=".4" fill="none">
        <polyline points="83,37 90,37 108,80"/>
        <polyline points="200,32 225,30"/>
        <polyline points="206,104 218,92 237,92"/>
        <polyline points="180,121 218,110 237,110"/>
        <polyline points="170,136 225,140"/>
      </g>
      <text class="chart-label" x="20" y="36">During Use of Item</text>
      <text class="chart-label" x="44" y="42">48%</text>
      <text class="chart-label" x="230" y="24">After Use,</text>
      <text class="chart-label" x="224" y="30">Before Disposal</text>
      <text class="chart-label" x="242" y="36">30%</text>
      <text class="chart-label" x="246" y="93">Disposal Related</text>
      <text class="chart-label" x="265" y="99">11%</text>
      <text class="chart-label" x="246" y="112">Recapping</text>
      <text class="chart-label" x="244" y="118">Used Needle</text>
      <text class="chart-label" x="260" y="124">3%</text>
      <text class="chart-label" x="234" y="140">Other</text>
      <text class="chart-label" x="236" y="146">8%</text>
    </svg>
    <div class="agency-mark">NHSB</div>
    <figcaption class="chart-caption">Figure 1: Activities associated with percutaneous injuries in SERNet hospitals, by % total percutaneous injuries (n= 951), 2007 (Source: <a>SERNet [2009]</a>).</figcaption>
  </figure>

  <footer class="footer">
    <span class="footer-company">Vantrel Medical, LLC</span>
    <span class="footer-product">SURGICAL STAPLE REMOVER</span>
  </footer>
</section>

<section class="slide slide--business">
  <svg class="header" viewBox="0 0 250 48" aria-hidden="true">
    <path d="M0 48 L0 34 Q22 28 30 0 L244 0 Q230 44 190 46 L0 48 Z" fill="var(--brand)"/>
    <path d="M0 34 Q22 28 30 0 L40 0 Q28 36 0 44 Z" fill="#fff" opacity=".25"/>
  </svg>
  <h1 class="header-title">The Business</h1>

  <svg class="icon" style="top:58px" width="26" height="26" viewBox="0 0 26 26" aria-hidden="true">
    <rect x="1" y="8" width="24" height="17" rx="2" fill="none" stroke="var(--brand)" stroke-width="1.6"/>
    <line x1="5" y1="4.5" x2="21" y2="4.5" stroke="var(--brand)" stroke-width="1.4"/>
    <line x1="3" y1="1.5" x2="23" y2="1.5" stroke="var(--brand)" stroke-width="1.4"/>
  </svg>

  <div class="business-copy">
    <p><span class="accent">Demand &amp; Necessity:</span> November 6, 2000 <b><i>The Needlestick Safety and Prevention Act</i></b> was passed to reduce injuries and prevent the transmission of bloodborn pathogens that result in viruses and disease.</p>
    <p><span class="accent">The law requires employers</span> to use work practice controls and safer devices that are engineered to eliminate or minimize exposure to bloodborne pathogens resulting from needlestick/sharp injuries.</p>
    <p style="margin-bottom:0"><span class="accent">Employers must:</span></p>
    <p class="indent"><span class="accent">-&gt; Demonstrate</span> that they are reviewing new technology that can reduce risk of exposure to bloodborne pathogens by updating exposure control plans and documenting the decision-making process on implementing such technology.</p>
    <p class="indent"><span class="accent">-&gt; Maintain</span> a sharps injury log to track the type and brand of device used, the department or area where the incident occurred, and an explanation of the incident. The log must be maintained in a manner to protect the confidentiality of the injured employee.</p>
    <p class="indent"><span class="accent">-&gt; Solicit</span> input from employees responsible for direct patient care in the identification, evaluation and selection of effective safety devices and work practice controls, as part of the ongoing exposure control plan development process. Efforts to encourage staff input must be documented in the plan.</p>
    <div class="callout">This means that when the SSR is available it must be used.</div>
    <p style="margin-bottom:0"><span class="accent">The cost of a sharps injury</span> can be a compelling reason to use safer sharps practices. One sharps injury can cause a number of direct and indirect costs for the health care facility, including:</p>
    <ul class="cost-list">
      <li>-&gt; Loss of employee time</li>
      <li>-&gt; Cost of tying up staff to investigate the injury</li>
      <li>-&gt; Expense of laboratory testing</li>
      <li>-&gt; Cost of treatment for infected staff</li>
      <li>-&gt; Cost of replacing staff</li>
    </ul>
  </div>

  <div class="seal" role="img" aria-label="National legislature badge"></div>
  <div class="agency-badge">Workplace<br>Safety Office</div>

  <footer class="footer">
    <span class="footer-company">Vantrel Medical, LLC</span>
    <span class="footer-product">SURGICAL STAPLE REMOVER</span>
  </footer>
</section>

</body>
</html>
```